Flyer design for corporate telephone business

We are a new company called "Harbourline Voice" that sells complete tailored phone solutions to businesses in Australia. In most cases we can also save many businesses 50%+ off their monthly telephone bill. They also get to keep their existing telephone numbers. We also provide complete new set-up of business phone equipment and services. So I would like these 3 points highlighted and to stand out. We utilise the latest technology with advanced features. The flyer should be A5 sized. Single sided. White background with mainly a lot of blue. Also a mixture of grey, a little bit of black etc. The final design should make the potential customer want to call us to find out more info.
Target Market(s)
Business Owners, Managers, Decision makers
Industry/Entity Type
Telecommunications
Requirements
Must have
- Flyer must highlight the 3 x call to actions. Below is order of priority
- 1. We help businesses save 50%+ on their monthly phone bill
- 2. Keep your existing telephone numbers
- 3. Brand new phone installation services or upgrades.
- Also contact details
- sales@harbourlinevoice.com.au
- ph: 58170926
Nice to have
- I would like to try and include as many product images attached to this brief as possible without making the flyer look to busy. I would like the customer to know that we can supply phones, video conferencing, headsets, etc Our logo is currently being designed on another project. This should be finished shortly and I can add this to the brief once I have the finished design.

```html
<!DOCTYPE html>
<html lang="en">
<head>
<meta charset="utf-8">
<title>Harbourline Voice – Business Phone Flyer</title>
<link href="https://fonts.googleapis.com/css2?family=Arimo:wght@400;700&display=swap" rel="stylesheet">
<style>
  :root {
    --blue: #1565c0;
    --blue-deep: #0d47a1;
    --blue-light: #6fa8dc;
    --blue-pale: #b9d3ee;
    --grey-soft: #e9eef4;
    --grey-text: #333a44;
    --white: #ffffff;
  }
  * { margin: 0; padding: 0; box-sizing: border-box; }
  html, body { width: 847px; height: 1200px; overflow: hidden; background: var(--white); }
  .flyer {
    position: relative; width: 847px; height: 1200px; overflow: hidden;
    font-family: "Arimo", Arial, sans-serif; color: var(--grey-text);
    background: linear-gradient(180deg, var(--grey-soft) 0%, var(--white) 28%, var(--white) 100%);
  }
  .decor { position: absolute; inset: 0; width: 847px; height: 1200px; }
  .logo-slot {
    position: absolute; left: 34px; top: 46px;
    font-size: 56px; font-weight: 400; color: var(--grey-text);
  }
  .brand-name {
    position: absolute; left: 510px; top: 58px;
    font-size: 33px; font-weight: 400; color: var(--blue);
  }
  .hero-photo {
    position: absolute; left: 430px; top: 110px; width: 400px; height: 400px;
    border-radius: 50%;
    background: radial-gradient(circle at 50% 45%, #f4f6f8 0%, #cfd6de 55%, #8a939e 100%);
  }
  .saving { position: absolute; left: 36px; top: 240px; }
  .saving-lead { font-size: 25px; color: var(--grey-text); padding-left: 14px; }
  .saving-main { font-size: 46px; font-weight: 700; color: var(--blue); line-height: 1.1; margin: 2px 0; }
  .saving-tail { font-size: 22px; color: var(--grey-text); padding-left: 70px; }
  .product-grid {
    position: absolute; left: 50px; top: 422px;
    display: grid; grid-template-columns: 218px 218px; grid-template-rows: 150px 150px; gap: 16px 28px;
  }
  .product-tile {
    border: 3px solid var(--blue-light); border-radius: 14px; background: var(--white);
    padding: 12px;
  }
  .product-tile .shot {
    width: 100%; height: 100%; border-radius: 8px;
    background: radial-gradient(circle at 50% 50%, #aab3bd 0%, #dfe4ea 60%, var(--white) 100%);
  }
  .supply-note {
    position: absolute; left: 72px; top: 752px; width: 420px;
    font-size: 21px; line-height: 1.2; color: var(--grey-text);
  }
  .keep-numbers {
    position: absolute; left: 30px; top: 828px; width: 430px;
    font-size: 42px; font-weight: 700; line-height: 1.2; color: var(--blue);
    letter-spacing: -0.5px;
  }
  .install-card {
    position: absolute; left: 580px; top: 652px; width: 252px; height: 362px;
    background: var(--white); border-radius: 4px;
    box-shadow: 0 4px 14px rgba(0,0,0,0.35);
    padding: 20px 16px;
    font-size: 38px; font-weight: 700; line-height: 63px; color: var(--blue);
  }
  .contact-details {
    position: absolute; left: 30px; top: 1075px;
    font-size: 22px; line-height: 1.4; color: var(--white);
  }
  .contact-details .label { font-weight: 700; color: var(--blue-deep); }
  .contact-phone {
    position: absolute; right: 40px; top: 1112px;
    font-size: 38px; font-weight: 700; color: var(--blue);
  }
</style>
</head>
<body>
<div class="flyer">
  <svg class="decor" viewBox="0 0 847 1200" aria-hidden="true">
    <path d="M0 210 C 150 150, 300 150, 440 210" fill="none" stroke="var(--blue)" stroke-width="6"/>
    <path d="M0 232 C 160 175, 300 178, 436 232" fill="none" stroke="var(--blue-pale)" stroke-width="10"/>
    <circle cx="630" cy="310" r="212" fill="none" stroke="var(--blue)" stroke-width="8"/>
    <circle cx="630" cy="310" r="226" fill="none" stroke="var(--blue-pale)" stroke-width="6"/>
    <path d="M0 1045 C 250 1020, 600 1020, 847 1045 L847 1200 L0 1200 Z" fill="var(--blue-light)"/>
    <path d="M0 1045 C 250 1020, 600 1020, 847 1045" fill="none" stroke="var(--blue)" stroke-width="4"/>
  </svg>

  <div class="logo-slot">Logo</div>
  <div class="brand-name">Harbourline Voice</div>

  <div class="hero-photo" role="img" aria-label="Group of modern business desk phones and a cordless handset"></div>

  <div class="saving">
    <p class="saving-lead">We help businesses</p>
    <p class="saving-main">save 50%+ on</p>
    <p class="saving-tail">your monthly phone bill...</p>
  </div>

  <div class="product-grid">
    <div class="product-tile"><div class="shot" role="img" aria-label="Video conferencing system with camera and speaker pods"></div></div>
    <div class="product-tile"><div class="shot" role="img" aria-label="Wireless office headset on its base"></div></div>
    <div class="product-tile"><div class="shot" role="img" aria-label="Colour-screen business desk phone"></div></div>
    <div class="product-tile"><div class="shot" role="img" aria-label="Cordless handset with base station"></div></div>
  </div>

  <p class="supply-note">we can supply phones, video conferencing, headsets, etc</p>

  <p class="keep-numbers">Keep your<br>existing telephone<br>numbers....</p>

  <div class="install-card">Brand new<br>phone<br>installation<br>services or<br>upgrades.</div>

  <div class="contact-details">
    <p class="label">Contact details:</p>
    <p>address........</p>
    <p>sales@harbourlinevoice.com.au</p>
  </div>
  <p class="contact-phone">phone: 58170926</p>
</div>
</body>
</html>
```